Wine Label for a White and a Red Wine from Italy

We have a very good idea of what we want with artwork. We need you to please design a 'template' with the text so we can change out the artwork from year to year. Samples are shown of what we are looking for. We are looking for options with the two basic designs. Brand name of wine is: Valora del Torrino. Both wines are in a light green Bordeaux-style bottle (note: we don't show a light green bottle in the mockup but please remember the bottle is light green). Artwork is provided. We'd like to see either the green or blue butterfly on the white wine, the red butterfly is for the red wine. Please base the design on the attached label from Ashby and/or the attached label from Chateau Vellanges.

Target Market(s)

Millennials, women

Requirements
Must have
• The artwork (butterflies) attached.
Nice to have
• Elegant, readable fonts. Please make the text so it can be changed by the printer. Please make it so the artwork can be changed too.

```html
<!DOCTYPE html>
<html lang="en">
<head>
<meta charset="utf-8">
<title>Valora del Torrino – Bianco Label</title>
<link href="https://fonts.googleapis.com/css2?family=Cormorant+Garamond:ital,wght@0,500;0,600;1,500;1,600&family=EB+Garamond:wght@400;500&display=swap" rel="stylesheet">
<style>
  :root {
    --page-bg: #f4efec;
    --label-white: #ffffff;
    --wine-red: #8a1424;
    --ink: #2a2422;
    --band-orange: #e99a1c;
    --band-gold: #f5c542;
    --art-orange: #e8a233;
    --art-gold: #f6d27a;
    --art-teal: #1f7f86;
  }
  * { margin: 0; padding: 0; box-sizing: border-box; }
  html, body {
    width: 1200px; height: 960px; overflow: hidden;
    background: var(--page-bg);
  }
  .label {
    position: absolute;
    left: 320px; top: 62px;
    width: 560px; height: 836px;
    background: var(--label-white);
    box-shadow: 0 4px 18px rgba(60, 40, 30, 0.12);
    color: var(--ink);
    text-align: center;
  }
  .label__band {
    position: absolute; left: 0; right: 0; height: 26px;
  }
  .label__band--top {
    top: 0;
    background: linear-gradient(to bottom, var(--band-orange), var(--band-gold) 55%, rgba(245,197,66,0));
  }
  .label__band--bottom {
    bottom: 0;
    background: linear-gradient(to top, var(--band-orange), var(--band-gold) 55%, rgba(245,197,66,0));
  }
  .line { position: absolute; left: 0; right: 0; line-height: 1; }
  .brand__name {
    top: 62px;
    font-family: "Cormorant Garamond", serif;
    font-style: italic; font-weight: 600;
    font-size: 70px; color: var(--wine-red);
  }
  .brand__sub {
    top: 132px;
    font-family: "Cormorant Garamond", serif;
    font-style: italic; font-weight: 600;
    font-size: 36px; color: var(--wine-red);
  }
  .selection {
    top: 198px;
    font-family: "EB Garamond", serif;
    font-size: 21px; letter-spacing: 0.22em;
    color: var(--ink);
  }
  .artwork {
    position: absolute;
    left: 95px; top: 232px;
    width: 370px; height: 316px;
    border-radius: 46% 40% 44% 48% / 42% 48% 40% 46%;
    background:
      radial-gradient(ellipse at 52% 46%, var(--art-teal) 0 14%, rgba(31,127,134,0) 26%),
      radial-gradient(ellipse at 50% 50%, var(--art-orange), var(--art-gold) 75%, rgba(246,210,122,0.2));
  }
  .vintage {
    top: 606px;
    font-family: "EB Garamond", serif;
    font-size: 34px; letter-spacing: 0.12em;
  }
  .varietal {
    top: 645px;
    font-family: "EB Garamond", serif;
    font-weight: 500;
    font-size: 44px; letter-spacing: 0.16em;
  }
  .region {
    top: 692px;
    font-family: "EB Garamond", serif;
    font-size: 25px;
  }
  .maker {
    top: 736px;
    font-family: "Cormorant Garamond", serif;
    font-style: italic; font-weight: 600;
    font-size: 27px; color: var(--wine-red);
  }
  .farming {
    top: 780px;
    font-family: "EB Garamond", serif;
    font-size: 23px;
  }
</style>
</head>
<body>
  <main class="label">
    <div class="label__band label__band--top"></div>

    <p class="line brand__name">Valora</p>
    <p class="line brand__sub">del Torrino</p>
    <p class="line selection">BARREL SELECTED</p>

    <div class="artwork" role="img" aria-label="Seasonal artwork: teal butterfly on a golden orange painted background"></div>

    <p class="line vintage">2018</p>
    <p class="line varietal">Bianco</p>
    <p class="line region">Piemonte, Italy</p>
    <p class="line maker">Artisanally crafted by Cantina Colle Alto</p>
    <p class="line farming">sustainably farmed</p>

    <div class="label__band label__band--bottom"></div>
  </main>
</body>
</html>
```